We need a tri-fold brochure for our business called: KindlePath. (KindlePath Therapy Services)
This is a therapy services business that offers Physiotherapy and Occupational Therapy to children aged 5 to 16 years of age. The focus is on Neuro-developmental therapy and the children have a range of conditions such as Cerebral-Palsy, brain injuries etc... We are looking for designs that focus on children, fun and the word nurture.
Target Market(s)
Primarily parents and people looking for therapy services.
Industry/Entity Type
Business
Font styles to use
Sans Serif

```html
<!DOCTYPE html>
<html lang="en">
<head>
<meta charset="utf-8">
<title>KindlePath Therapy Services – Brand Set</title>
<link href="https://fonts.googleapis.com/css2?family=Open+Sans:wght@300;400;600;700;800&display=swap" rel="stylesheet">
<style>
:root{
  --stage:#a7a8ab;
  --white:#ffffff;
  --green:#8cc63f;
  --green-deep:#7bb52f;
  --orange:#f7941d;
  --blue:#2f7fd3;
  --blue-deep:#1f6cc4;
  --sky:#29a8e0;
  --ink:#333333;
  --muted:#555555;
}
*{margin:0;padding:0;box-sizing:border-box}
html,body{width:1200px;height:1200px;overflow:hidden;background:var(--stage)}
body{font-family:"Open Sans",Arial,sans-serif;color:var(--ink)}
.canvas{position:relative;width:1200px;height:1200px;overflow:hidden;background:var(--stage)}
.abs{position:absolute}
.shadow{box-shadow:2px 3px 6px rgba(0,0,0,.28)}

/* brand lockup */
.brand-name{font-weight:400;letter-spacing:.01em;line-height:1;text-transform:uppercase;white-space:nowrap}
.brand-tag{font-weight:400;text-transform:uppercase;white-space:nowrap;line-height:1}
.brand-mark{border-radius:50%;border:3px solid var(--orange)}

/* logo card */
.logo-card{left:21px;top:0;width:393px;height:489px;background:var(--white)}
.logo-card .brand-mark{left:121px;top:150px;width:150px;height:150px;border-width:5px}
.logo-card .brand-name{left:0;width:393px;top:355px;text-align:center;font-size:44px;color:var(--green)}
.logo-card .brand-tag{left:0;width:393px;top:398px;text-align:center;font-size:16px;letter-spacing:.62em;color:var(--muted);padding-left:10px}

/* business cards */
.biz-front{left:54px;top:550px;width:320px;height:183px;background:var(--white);overflow:hidden}
.biz-front .brand-mark{left:55px;top:25px;width:32px;height:32px}
.biz-front .brand-name{left:0;width:142px;top:80px;text-align:center;font-size:11px;color:var(--orange)}
.biz-front .brand-tag{left:0;width:142px;top:93px;text-align:center;font-size:5px;letter-spacing:.4em;color:var(--muted)}
.biz-front .person{left:20px;top:135px;color:var(--white)}
.person-name{font-size:20px;font-weight:300;line-height:1}
.person-title{font-size:8.5px;margin-top:3px}
.contact{font-size:8.5px;color:var(--white);line-height:10.5px}
.contact td{padding:0;vertical-align:top}
.contact td.label{font-weight:700;width:38px}
.biz-front .contact{left:176px;top:104px;font-size:8px}
.biz-front .contact td.label{width:37px}
.biz-front .address{left:176px;top:145px;font-size:8.5px;line-height:10.5px;color:var(--white)}

.biz-back{left:54px;top:751px;width:320px;height:183px;overflow:hidden}
.biz-back .photo{inset:0;background:linear-gradient(135deg,#2a7bd0 0%,#3b86d6 55%,#2a6fc2 100%)}
.biz-back .brand-mark{left:132px;top:42px;width:50px;height:50px;border-width:4px}
.biz-back .brand-name{left:0;width:320px;top:116px;text-align:center;font-size:18px;color:var(--orange)}
.biz-back .brand-tag{left:0;width:320px;top:137px;text-align:center;font-size:7px;letter-spacing:.45em;color:var(--white)}

/* brochure */
.brochure{left:471px;width:667px;height:517px;display:flex;overflow:hidden}
.brochure.outside{top:70px}
.brochure.inside{top:612px}
.panel{position:relative;width:222.3px;height:517px;overflow:hidden}
.photo{position:absolute}
.h-panel{font-weight:700;font-size:20px;line-height:1;text-transform:uppercase}
.sub{font-size:10px;line-height:1.2}
.body-copy{font-size:8.6px;line-height:10.9px}
.justify{text-align:justify}
.center{text-align:center}
.front{z-index:2}

/* outside panel 1 */
.out-1{background:var(--white)}
.out-1 .h-panel{left:23px;top:30px;color:var(--green)}
.out-1 .sub{left:23px;top:54px;color:var(--ink)}
.out-1 .intro{left:23px;top:77px;width:176px}
.out-1 .callout{left:23px;top:155px;width:176px;height:90px;background:var(--orange);color:var(--white);font-size:7.7px;line-height:10px;padding:9px 12px;text-align:center}
.out-1 .closing{left:40px;top:262px;width:142px}
.specialty{font-size:12px;line-height:15px;text-transform:uppercase}
.specialty .a{color:var(--sky)}
.specialty .b{color:var(--orange)}
.out-1 .specialty{left:0;width:222px;top:318px;text-align:center}
.out-1 .photo{left:0;top:362px;width:222px;height:155px;background:linear-gradient(120deg,#f4d7c4 0%,#c9b9ad 45%,#6d8fa8 100%)}

/* outside panel 2 */
.out-2{background:var(--blue)}
.out-2 .photo{inset:0;background:linear-gradient(160deg,#3b86d6 0%,#2f7fd3 50%,#2a74c9 100%)}
.out-2 .h-panel{left:30px;top:143px;color:var(--green)}
.out-2 .sub{left:30px;top:167px;color:var(--white)}
.out-2 .intro{left:30px;top:182px;width:141px;color:var(--white)}
.out-2 .brand-mark{left:83px;top:315px;width:60px;height:60px;border-width:4px}
.out-2 .brand-name{left:0;width:222px;top:388px;text-align:center;font-size:18px;color:var(--orange)}
.out-2 .brand-tag{left:0;width:222px;top:409px;text-align:center;font-size:7.5px;letter-spacing:.42em;color:var(--white)}
.out-2 .contact{left:30px;top:434px}
.out-2 .address{left:30px;top:478px;font-size:8.5px;line-height:10.5px;color:var(--white)}

/* outside panel 3 (cover) */
.out-3{background:var(--white)}
.out-3 .brand-mark{left:78px;top:20px;width:68px;height:68px;border-width:4px}
.out-3 .brand-name{left:0;width:222px;top:100px;text-align:center;font-size:18px;color:var(--orange)}
.out-3 .brand-tag{left:0;width:222px;top:120px;text-align:center;font-size:7.5px;letter-spacing:.42em;color:var(--muted)}
.out-3 .specialty{left:0;width:222px;top:134px;text-align:center}
.out-3 .photo{left:0;top:180px;width:222px;height:337px;background:linear-gradient(150deg,#e9e4de 0%,#d8c3b1 40%,#c9a58b 65%,#d94b4b 88%,#e2c13a 100%)}

/* inside panel 1 */
.in-1{background:var(--sky);color:var(--white)}
.in-1 .photo{left:0;top:0;width:222px;height:240px;background:linear-gradient(135deg,#f2eee8 0%,#d8c8b4 45%,#b79d80 75%,#9c8a74 100%)}
.in-1 .h-panel{left:19px;top:256px;color:var(--white)}
.in-1 .sub{left:19px;top:278px}
.in-1 .copy{left:19px;top:300px;width:185px}
.minor{font-weight:700;font-size:9.5px;line-height:12px;margin-top:11px}
.copy p + p{margin-top:7px}

/* inside panel 2 */
.in-2{background:var(--white)}
.in-2 .photo{left:0;top:0;width:222px;height:126px;background:linear-gradient(120deg,#dfe7ef 0%,#f0d5a6 40%,#7fb3d8 75%,#f2e04a 100%)}
.in-2 .h-panel{left:0;width:222px;top:129px;text-align:center;color:var(--orange)}
.in-2 .sub{left:0;width:222px;top:151px;text-align:center;color:var(--ink)}
.features{left:13px;top:170px;width:197px;display:grid;grid-template-columns:repeat(3,62px);grid-auto-rows:62px;gap:5px 4px}
.feature{color:var(--white);font-size:7px;line-height:7.5px;text-align:center;display:flex;flex-direction:column;align-items:center;justify-content:flex-end;padding-bottom:6px}
.feature svg{margin-bottom:auto;margin-top:8px}
.feature.green{background:var(--green)}
.feature.blue{background:var(--sky)}
.in-2 .h-small{left:27px;top:343px;font-weight:700;font-size:15px;color:var(--orange);text-transform:uppercase;line-height:1}
.in-2 .quote-open{left:27px;top:368px}
.in-2 .quote-close{left:188px;top:448px}
.in-2 .testimonial{left:27px;top:381px;width:178px;color:var(--ink)}
.in-2 .cite{left:27px;top:462px;font-size:8px;line-height:10px;color:var(--ink)}
.cite b{color:var(--sky);font-weight:700}

/* inside panel 3 */
.in-3{background:var(--green);color:var(--white)}
.in-3 .photo{inset:0;background:linear-gradient(160deg,#8cc63f 0%,#93c94a 50%,#85bf3a 100%)}
.in-3 .h-panel{left:19px;top:20px;color:var(--white)}
.in-3 .sub{left:19px;top:42px}
.in-3 .intro{left:19px;top:69px;width:188px}
.in-3 .minor-block{left:19px;top:108px;width:190px}
.value{left:19px;width:200px;display:flex;gap:12px}
.value .badge{flex:0 0 42px;height:42px;border-radius:50%;background:var(--white);display:flex;align-items:center;justify-content:center;margin-top:6px}
.value h4{font-size:9.5px;font-weight:700;text-transform:uppercase;line-height:11px}
.value p{font-size:7.8px;line-height:10px}
.in-3 .v1{top:210px}
.in-3 .v2{top:278px}
.in-3 .v3{top:345px}
.in-3 .closing-bold{left:19px;top:420px;width:190px;font-weight:700}
.in-3 .closing{left:19px;top:466px;width:190px}
</style>
</head>
<body>
<div class="canvas">

  <!-- Identity card -->
  <section class="abs logo-card shadow" aria-label="KindlePath brand identity">
    <div class="abs brand-mark" aria-hidden="true"></div>
    <div class="abs brand-name">KindlePath</div>
    <div class="abs brand-tag">Therapy Services</div>
  </section>

  <!-- Business card front -->
  <section class="abs biz-front shadow" aria-label="Business card front">
    <svg class="abs" style="left:0;top:0" width="320" height="183" viewBox="0 0 320 183" aria-hidden="true">
      <path d="M0,110 C90,130 160,112 205,70 C245,34 280,18 320,16 L320,23 C283,25 250,40 212,76 C168,118 96,138 0,120 Z" fill="var(--orange)"/>
      <path d="M0,120 C96,138 168,118 212,76 C250,40 283,25 320,23 L320,183 L0,183 Z" fill="var(--blue-deep)"/>
      <path d="M0,114 C80,132 140,124 180,104 C130,126 70,132 0,124 Z" fill="var(--green)"/>
    </svg>
    <div class="abs brand-mark" aria-hidden="true"></div>
    <div class="abs brand-name">KindlePath</div>
    <div class="abs brand-tag">Therapy Services</div>
    <table class="abs contact">
      <tr><td class="label">Phone</td><td>123-456-7890</td></tr>
      <tr><td class="label">Fax</td><td>123-456-7890</td></tr>
      <tr><td class="label">Email</td><td>info@kindlepath.example</td></tr>
    </table>
    <div class="abs address">address line 1 goes here<br>PoBox address 12345</div>
    <div class="abs person">
      <div class="person-name">NAME HERE</div>
      <div class="person-title">Designation Title</div>
    </div>
  </section>

  <!-- Business card back -->
  <section class="abs biz-back shadow" aria-label="Business card back">
    <div class="abs photo" role="img" aria-label="Faint blue-toned photo of a child at play"></div>
    <div class="abs brand-mark" aria-hidden="true"></div>
    <div class="abs brand-name">KindlePath</div>
    <div class="abs brand-tag">Therapy Services</div>
  </section>

  <!-- Brochure outside -->
  <section class="abs brochure outside shadow" aria-label="Brochure outside spread">
    <article class="panel out-1">
      <div class="photo" role="img" aria-label="Photo of a therapist playing with a toddler using finger puppets"></div>
      <svg class="abs" style="left:0;top:352px" width="222" height="44" viewBox="0 0 222 44" aria-hidden="true">
        <path d="M0,0 L222,0 L222,22 C150,36 60,34 0,10 Z" fill="var(--white)"/>
        <path d="M0,2 C60,28 150,32 222,16 L222,24 C150,40 60,38 0,14 Z" fill="var(--green)"/>
      </svg>
      <h2 class="abs h-panel">Lorem Ipsum</h2>
      <div class="abs sub">Dolor Set Emet</div>
      <p class="abs body-copy justify intro">Lorem ipsum dolor sit amet, consectetur adipiscing elit, sed do eiusmod tempor incididunt ut labore et dolore magna aliqua. Ut enim ad minim veniam, quis nostrud exercitation ullamco laboris nisi ut aliquip ex ea commodo consequat.</p>
      <div class="abs callout">Lorem ipsum dolor sit amet, consectetur adipiscing elit, sed do eiusmod tempor incididunt ut labore et dolore magna aliqua. Ut enim ad minim veniam, quis nostrud exercitation ullamco laboris nisi ut aliquip ex ea commodo consequat.</div>
      <p class="abs body-copy center closing">Lorem ipsum dolor sit amet, consectetur adipiscing elit, sed do eiusmod tempor incididunt ut labore et dolore magna aliqua.</p>
      <div class="abs specialty front"><span class="a">Neuro-Developmental</span><br><span class="b">Therapy</span></div>
    </article>

    <article class="panel out-2">
      <div class="photo" role="img" aria-label="Faint blue-toned photo of a child with a therapist"></div>
      <h2 class="abs h-panel">Lorem Ipsum</h2>
      <div class="abs sub">Dolor Set Emet</div>
      <p class="abs body-copy justify intro">Lorem ipsum dolor sit amet, consectetur adipiscing elit, sed do eiusmod tempor incididunt ut labore et dolore magna aliqua. Ut enim ad minim veniam, quis nostrud exercitation ullamco laboris nisi ut aliquip ex ea commodo consequat.</p>
      <div class="abs brand-mark" aria-hidden="true"></div>
      <div class="abs brand-name">KindlePath</div>
      <div class="abs brand-tag">Therapy Services</div>
      <table class="abs contact">
        <tr><td class="label" style="font-weight:400">Phone</td><td>123-456-7890</td></tr>
        <tr><td class="label" style="font-weight:400">Fax</td><td>123-456-7890</td></tr>
        <tr><td class="label" style="font-weight:400">Email</td><td>info@kindlepath.example</td></tr>
      </table>
      <div class="abs address">address line 1 goes here<br>PoBox address 12345</div>
    </article>

    <article class="panel out-3">
      <div class="photo" role="img" aria-label="Photo of a smiling mother and young daughter playing with building blocks"></div>
      <svg class="abs" style="left:0;top:170px" width="222" height="80" viewBox="0 0 222 80" aria-hidden="true">
        <path d="M0,0 L222,0 L222,0 C150,8 60,26 0,52 Z" fill="var(--white)"/>
        <path d="M0,52 C60,26 150,8 222,0 L222,14 C150,16 70,32 0,58 Z" fill="var(--orange)"/>
      </svg>
      <div class="abs brand-mark" aria-hidden="true"></div>
      <div class="abs brand-name">KindlePath</div>
      <div class="abs brand-tag">Therapy Services</div>
      <div class="abs specialty front"><span class="a">Neuro-Developmental</span><br><span class="b">Therapy</span></div>
    </article>
  </section>

  <!-- Brochure inside -->
  <section class="abs brochure inside shadow" aria-label="Brochure inside spread">
    <article class="panel in-1">
      <div class="photo" role="img" aria-label="Photo of a mother and son building a tower with wooden blocks"></div>
      <svg class="abs" style="left:0;top:140px" width="222" height="100" viewBox="0 0 222 100" aria-hidden="true">
        <path d="M0,84 C90,78 170,50 222,0 L222,100 L0,100 Z" fill="var(--orange)"/>
        <path d="M0,92 C90,86 175,58 222,10 L222,100 L0,100 Z" fill="var(--sky)"/>
      </svg>
      <h2 class="abs h-panel">About Company</h2>
      <div class="abs sub">Short Summary</div>
      <div class="abs copy body-copy">
        <p>Ut enim ad minim veniam, quis nostrud exercitation ullamco laboris nisi ut aliquip ex ea commodo consequat.</p>
        <div class="minor">Lorem Ipsum</div>
        <p style="margin-top:2px">Lorem ipsum dolor sit amet, consectetur adipiscing elit, sed do eiusmod tempor incididunt ut labore et dolore magna aliqua. Ut enim ad minim veniam, quis nostrud exercitation ullamco laboris nisi ut aliquip ex ea commodo consequat.</p>
        <p style="margin-top:7px">Lorem ipsum dolor sit amet, consectetur adipiscing elit, sed do eiusmod tempor incididunt ut labore et dolore magna aliqua. Ut enim ad minim veniam, quis nostrud exercitation ullamco laboris nisi ut aliquip ex ea commodo consequat.</p>
      </div>
    </article>

    <article class="panel in-2">
      <div class="photo" role="img" aria-label="Photo of children in a bright therapy room with exercise balls"></div>
      <svg class="abs" style="left:0;top:72px" width="222" height="56" viewBox="0 0 222 56" aria-hidden="true">
        <path d="M0,50 C40,22 140,10 222,24 L222,56 L0,56 Z" fill="var(--white)"/>
        <path d="M0,44 C40,14 140,2 222,16 L222,24 C140,10 40,22 0,50 Z" fill="var(--green)"/>
      </svg>
      <h2 class="abs h-panel">Why Choose Us</h2>
      <div class="abs sub">What We Do For You</div>
      <div class="abs features">
        <div class="feature green">
          <svg width="20" height="20" viewBox="0 0 20 20" aria-hidden="true"><rect x="2" y="3" width="16" height="15" rx="2" fill="none" stroke="#fff" stroke-width="2"/><rect x="2" y="3" width="16" height="4" fill="#fff"/><text x="10" y="16" font-size="7" font-weight="700" text-anchor="middle" fill="#fff" font-family="Open Sans, sans-serif">14</text></svg>
          <span>Fast Same<br>Day Service</span>
        </div>
        <div class="feature blue">
          <svg width="20" height="20" viewBox="0 0 20 20" aria-hidden="true"><circle cx="10" cy="6" r="4" fill="#fff"/><path d="M2,18 C2,12 18,12 18,18 Z" fill="#fff"/></svg>
          <span>Friendly<br>Trained<br>Workers</span>
        </div>
        <div class="feature green">
          <svg width="20" height="20" viewBox="0 0 20 20" aria-hidden="true"><path d="M2,9 L10,2 L18,9" fill="none" stroke="#fff" stroke-width="2"/><rect x="5" y="9" width="10" height="9" fill="none" stroke="#fff" stroke-width="2"/></svg>
          <span>Free In<br>Home<br>Estimates</span>
        </div>
        <div class="feature blue">
          <svg width="20" height="20" viewBox="0 0 20 20" aria-hidden="true"><circle cx="10" cy="7" r="4" fill="none" stroke="#fff" stroke-width="2"/><path d="M3,18 C3,13 17,13 17,18" fill="none" stroke="#fff" stroke-width="2"/></svg>
          <span>Phone Advice<br>Call Anytime</span>
        </div>
        <div class="feature green">
          <svg width="20" height="20" viewBox="0 0 20 20" aria-hidden="true"><rect x="3" y="3" width="9" height="15" fill="none" stroke="#fff" stroke-width="2"/><rect x="12" y="8" width="5" height="10" fill="none" stroke="#fff" stroke-width="2"/><rect x="6" y="6" width="3" height="3" fill="#fff"/><rect x="6" y="11" width="3" height="3" fill="#fff"/></svg>
          <span>Local Small<br>Business</span>
        </div>
        <div class="feature blue">
          <svg width="20" height="20" viewBox="0 0 20 20" aria-hidden="true"><rect x="2" y="9" width="4" height="9" fill="#fff"/><path d="M7,9 L11,2 C13,2 13,4 12,8 L17,8 C18,8 18,10 17,11 L16,17 C16,18 15,18 14,18 L7,18 Z" fill="#fff"/></svg>
          <span>We do the<br>job right,<br>every time!</span>
        </div>
      </div>
      <h3 class="abs h-small">User Testimonial</h3>
      <svg class="abs quote-open" width="12" height="10" viewBox="0 0 12 10" aria-hidden="true"><path d="M0,10 L0,5 C0,2 2,0 5,0 L5,2 C3,2 3,4 3,5 L5,5 L5,10 Z M7,10 L7,5 C7,2 9,0 12,0 L12,2 C10,2 10,4 10,5 L12,5 L12,10 Z" fill="var(--orange)"/></svg>
      <p class="abs body-copy testimonial">Lorem ipsum dolor sit amet, consectetur adipiscing elit, sed do eiusmod tempor incididunt ut labore et dolore magna aliqua. Ut enim ad minim veniam, quis nostrud exercitation ullamco laboris nisi ut aliquip ex ea commodo consequat.</p>
      <svg class="abs quote-close" width="12" height="10" viewBox="0 0 12 10" aria-hidden="true"><path d="M12,0 L12,5 C12,8 10,10 7,10 L7,8 C9,8 9,6 9,5 L7,5 L7,0 Z M5,0 L5,5 C5,8 3,10 0,10 L0,8 C2,8 2,6 2,5 L0,5 L0,0 Z" fill="var(--orange)"/></svg>
      <div class="abs cite"><b>XYZ Name</b><br>Company Name<br>Country</div>
    </article>

    <article class="panel in-3">
      <div class="photo" role="img" aria-label="Faint green-toned photo of children playing"></div>
      <h2 class="abs h-panel">Key to Sucess</h2>
      <div class="abs sub">What Makes Us Successful</div>
      <p class="abs body-copy intro">Ut enim ad minim veniam, quis nostrud exercitation ullamco laboris nisi ut aliquip ex ea commodo consequat.</p>
      <div class="abs body-copy minor-block"><div class="minor" style="margin-top:0">Lorem Ipsum</div>Lorem ipsum dolor sit amet, consectetur adipiscing elit, sed do eiusmod tempor incididunt ut labore et dolore magna aliqua. Ut enim ad minim veniam, quis nostrud exercitation ullamco laboris nisi ut aliquip ex ea commodo consequat.</div>
      <div class="abs value v1">
        <div class="badge"><svg width="22" height="22" viewBox="0 0 22 22" aria-hidden="true"><rect x="3" y="3" width="16" height="16" rx="2" fill="none" stroke="var(--green)" stroke-width="2"/><path d="M6,11 L10,15 L17,6" fill="none" stroke="var(--green)" stroke-width="2.5"/></svg></div>
        <div><h4>Consitency</h4><p>Lorem ipsum dolor sit amet, consectetur adipiscing elit, sed do eiusmod tempor incididunt ut labore et dolore magna aliqua.</p></div>
      </div>
      <div class="abs value v2">
        <div class="badge"><svg width="24" height="24" viewBox="0 0 24 24" aria-hidden="true"><circle cx="12" cy="12" r="10" fill="none" stroke="var(--green)" stroke-width="2"/><circle cx="12" cy="12" r="6" fill="none" stroke="var(--green)" stroke-width="2"/><circle cx="12" cy="12" r="2.5" fill="var(--green)"/></svg></div>
        <div><h4>Accuracy</h4><p>Lorem ipsum dolor sit amet, consectetur adipiscing elit, sed do eiusmod tempor incididunt ut labore et dolore magna aliqua.</p></div>
      </div>
      <div class="abs value v3">
        <div class="badge"><svg width="24" height="24" viewBox="0 0 24 24" aria-hidden="true"><circle cx="12" cy="12" r="10" fill="none" stroke="var(--green)" stroke-width="2"/><path d="M12,6 L13.8,10.2 L18,10.5 L14.8,13.3 L15.8,17.5 L12,15.2 L8.2,17.5 L9.2,13.3 L6,10.5 L10.2,10.2 Z" fill="var(--green)"/></svg></div>
        <div><h4>Quality</h4><p>Lorem ipsum dolor sit amet, consectetur adipiscing elit, sed do eiusmod tempor incididunt ut labore et dolore magna aliqua.</p></div>
      </div>
      <p class="abs body-copy closing-bold">Lorem ipsum dolor sit amet, consectetur adipiscing elit, sed do eiusmod tempor incididunt ut labore et dolore magna.</p>
      <p class="abs body-copy closing">Ut enim ad minim veniam, quis nostrud exercitation ullamco laboris nisi ut aliquip ex ea commodo consequat.</p>
    </article>
  </section>

</div>
</body>
</html>
```